Anzeigengestaltung für Brötchen- und Brotlieferant
Zielgruppe
Wir beliefern Privatkunden Freitag, Samstag und Sonntag mit Brötchen / Broten und suchen ein Design für eine Werbekampagne zur Neukundengewinnung über Facebook. Sprich ein Bild indem alles kurz und knapp für den Kunden erklärt wird und man damit Werbung schalten kann.

```html
<!DOCTYPE html>
<html lang="de">
<head>
<meta charset="utf-8">
<title>Brötchenservice – Anzeige</title>
<link href="https://fonts.googleapis.com/css2?family=Oswald:wght@300;400;500;700&display=swap" rel="stylesheet">
<style>
  :root {
    --peach: #fecb9b;
    --brown: #7a3323;
    --text-brown: #6e2e1f;
    --white: #ffffff;
    --bread-light: #d99a5c;
    --bread-mid: #b8703b;
    --bread-dark: #8a4a25;
  }
  html, body { margin: 0; padding: 0; overflow: hidden; }
  body { width: 1200px; height: 846px; background: var(--white); }
  .ad {
    position: relative; width: 1200px; height: 846px; overflow: hidden;
    font-family: 'Oswald', sans-serif; color: var(--text-brown);
  }
  .ad__backdrop { position: absolute; inset: 0; }
  .ad__title {
    position: absolute; left: 28px; top: 36px; margin: 0;
    font-weight: 700; font-size: 64px; line-height: 1; color: var(--brown);
    transform: scaleX(0.84); transform-origin: left top; white-space: nowrap;
  }
  .ad__subtitle {
    position: absolute; left: 28px; top: 140px; margin: 0;
    font-weight: 400; font-size: 43px; line-height: 50px; color: var(--brown);
  }
  .ad__lead {
    position: absolute; left: 28px; top: 266px; margin: 0;
    font-weight: 300; font-size: 38px; line-height: 46px; letter-spacing: -0.5px;
  }
  .ad__detail {
    position: absolute; left: 28px; top: 428px; margin: 0;
    font-weight: 300; font-size: 30px; line-height: 43px; letter-spacing: -0.5px;
  }
  .ad__contact { position: absolute; left: 28px; top: 638px; }
  .ad__cta {
    margin: 0 0 4px; font-weight: 700; font-size: 30px; line-height: 38px;
    color: var(--brown); letter-spacing: -0.6px;
  }
  .ad__contact-line {
    margin: 0; font-weight: 300; font-size: 31px; line-height: 37px; letter-spacing: -0.6px;
  }
  .badge {
    position: absolute; left: 417px; top: 510px; width: 266px; height: 266px;
    border-radius: 50%; background: var(--white);
  }
  .badge__inner {
    position: absolute; inset: 7px; border-radius: 50%; background: var(--brown);
    display: flex; align-items: center; justify-content: center; text-align: center;
    color: var(--peach); font-weight: 400; font-size: 32px; line-height: 43px;
    letter-spacing: -0.5px;
  }
  .brand {
    position: absolute; left: 1029px; top: 46px; width: 160px; text-align: center;
    color: var(--brown); font-weight: 400;
  }
  .brand__circle {
    width: 86px; height: 86px; margin: 0 auto 6px; border-radius: 50%;
    background: var(--peach);
  }
  .brand__name { font-size: 17px; line-height: 1; }
</style>
</head>
<body>
<div class="ad">
  <svg class="ad__backdrop" width="1200" height="846" viewBox="0 0 1200 846">
    <defs>
      <radialGradient id="breadTones" cx="860" cy="560" r="560" gradientUnits="userSpaceOnUse">
        <stop offset="0" stop-color="var(--bread-light)"/>
        <stop offset="0.45" stop-color="var(--bread-mid)"/>
        <stop offset="0.75" stop-color="#e3b48a"/>
        <stop offset="1" stop-color="var(--white)"/>
      </radialGradient>
    </defs>
    <rect class="panel-peach" x="0" y="0" width="1200" height="846" fill="var(--peach)"/>
    <polygon class="panel-white" points="462,0 1200,0 1200,846 586,846" fill="var(--white)"/>
    <polygon role="img" aria-label="Foto: Weidenkorb mit frisch gebackenen Broten und Brötchen, vorn ein angeschnittenes Körnerbrot"
             points="462,0 1200,0 1200,846 586,846" fill="url(#breadTones)"/>
  </svg>

  <h1 class="ad__title">Brötchenservice</h1>
  <h2 class="ad__subtitle">Ofenfrisches Brot für<br>Sie zu Hause</h2>
  <p class="ad__lead">Lassen Sie sich Ihr Brot und Ihre<br>Brötchen am Freitag, Samstag und<br>Sonntag frisch nach Hause liefern.</p>
  <p class="ad__detail">Ihre Backwaren werden in unserer<br>Partnerbäckerei Krumbholz in Nieder-Lindau für<br>Sie verpackt und danach ausgeliefert.</p>

  <div class="ad__contact">
    <p class="ad__cta">Bestellen Sie jetzt</p>
    <p class="ad__contact-line">035123 / 48 62 17</p>
    <p class="ad__contact-line">kontakt@broetchenservice-hellmer.de</p>
    <p class="ad__contact-line">https://www.broetchenservice-hellmer.de/</p>
  </div>

  <div class="badge">
    <div class="badge__inner">KOSTENLOSE<br>PROBEBESTELLUNG</div>
  </div>

  <div class="brand">
    <div class="brand__circle"></div>
    <div class="brand__name">Jonas Hellmer</div>
  </div>
</div>
</body>
</html>
```